Forward thinking startup needs business cards

We are a new company entering the fall protection market and we need business cards. We provide equipment and supplies to a very large industry, and we aim to catch the attention of the end-user; not just the distributors. Please browse brovanteq.com for a better feel of our initial branding. The hog images are not required, but are here for inspiration. Also, they should not be prominent in the design as much as an accent. Many of our customers will be very high-end, so this should be considered as well.

Target Market(s)

Buyers for the safety industry. Some accounts will be very large, but most of these people are very down-to-earth.

Industry/Entity Type

Business

Contact Information for Business Card

Name and title
phone: 1-800-563-2814
fax: 740-318-5096
web: www.brovanteq.com
address: 712 Quarrybend Lane, Waterford, OH 45786 USA
room for cell number, direct office phone number, extension, and email

Font styles to use
Serif
Sans Serif

Colors
f37122
ffffff

Requirements
Must have
• Should be very clean and easy to read. We typically use orange and grey in our color schemes - #ef7c2d and #424242
Nice to have
• It would be nice to have room somewhere to incorporate some of the other logos from our family of companies. At the same time, it should not look weird if they aren't included.

```html
<!DOCTYPE html>
<html lang="en">
<head>
<meta charset="utf-8">
<title>Brovanteq Business Card</title>
<link rel="stylesheet" href="https://fonts.googleapis.com/css2?family=Source+Sans+3:wght@400;600;700&display=swap">
<style>
  :root {
    --orange: #f37122;
    --grey: #424242;
    --charcoal: #2a2a2a;
    --white: #ffffff;
    --ink: #3a3a3a;
    --backdrop: #e6e4e1;
  }
  html, body {
    margin: 0;
    padding: 0;
    width: 1200px;
    height: 1200px;
    overflow: hidden;
    background: var(--backdrop);
    font-family: "Source Sans 3", Arial, sans-serif;
  }
  .canvas {
    width: 1200px;
    height: 1200px;
    display: flex;
    flex-direction: column;
    align-items: center;
    justify-content: center;
    gap: 70px;
  }
  .card {
    position: relative;
    width: 760px;
    height: 434px;
    box-shadow: 0 6px 20px rgba(0,0,0,0.18);
    overflow: hidden;
  }
  /* Back side */
  .card-back {
    background:
      repeating-linear-gradient(180deg, rgba(255,255,255,0.035) 0 1px, transparent 1px 4px),
      var(--charcoal);
    display: flex;
    align-items: center;
    justify-content: center;
  }
  .brand-name-large {
    color: var(--white);
    font-weight: 700;
    font-size: 92px;
    letter-spacing: 3px;
    text-transform: uppercase;
  }
  /* Front side */
  .card-front {
    background: var(--white);
  }
  .card-front .decor {
    position: absolute;
    inset: 0;
  }
  .identity {
    position: absolute;
    left: 92px;
    top: 34px;
  }
  .person-name {
    margin: 0;
    color: var(--orange);
    font-weight: 600;
    font-size: 28px;
    line-height: 1.05;
  }
  .person-title {
    margin: 0;
    color: var(--ink);
    font-size: 19px;
    line-height: 1.2;
  }
  .contact {
    position: absolute;
    left: 40px;
    top: 178px;
    color: var(--ink);
    font-size: 18px;
    line-height: 1.32;
  }
  .contact p { margin: 0; }
  .contact .gap { margin-top: 8px; }
  .contact .label { color: var(--orange); }
  .brand-name-small {
    position: absolute;
    right: 56px;
    top: 160px;
    color: var(--orange);
    font-weight: 700;
    font-size: 50px;
    letter-spacing: 1px;
    text-transform: uppercase;
  }
</style>
</head>
<body>
<main class="canvas">
  <section class="card card-back" aria-label="Card back">
    <span class="brand-name-large">Brovanteq</span>
  </section>

  <section class="card card-front" aria-label="Card front">
    <svg class="decor" width="760" height="434" viewBox="0 0 760 434" aria-hidden="true">
      <polygon points="40,34 78,34 40,72" fill="var(--orange)"/>
      <polygon points="78,34 78,72 40,72" fill="var(--grey)"/>
      <polygon points="0,322 262,322 286,352 0,352" fill="var(--orange)"/>
      <polygon points="262,340 760,340 760,434 318,434" fill="var(--grey)"/>
    </svg>

    <div class="identity">
      <p class="person-name">Dana Whitfield</p>
      <p class="person-title">Managing Director</p>
    </div>

    <div class="contact">
      <p>712 Quarrybend Lane</p>
      <p>Waterford, OH 45786 USA</p>
      <p class="gap"><span class="label">p:</span> 1-800-563-2814</p>
      <p><span class="label">f:</span> 740-318-5096</p>
      <p><span class="label">e:</span> info@brovanteq.com</p>
    </div>

    <span class="brand-name-small">Brovanteq</span>
  </section>
</main>
</body>
</html>
```